Fast Money - Simple Book Cover Design

Hello,

I am in need of a cover for my new book. The Book Title Is

"Standing Growth - Keys to Glowing Customer Ratings That Fill The Calendar and Draw Fresh Clients Through Every Entrance!"

Author: Fireman Dale Orsworth

What I want: This is a book for businesses on improving their online reputation. I want to have 5 Stars on the cover. You can look at this quarvex search for ideas of what I am meaning.....

(copy and paste)

http://www.quarvex-find.example/search?q=5+star+online+reviews&mode=images&ref=kx7Lp2QwZt9 (copy and paste)

I am open to different color schemes for the book. I am partial to dark blues if you make it look good. Here is another book that I really like the cover of....

http://www.brindlemart.example/Clipwave-Tactics-Earning-Promotion-ebook/item/Z93KT4WQPX

I want the cover BOLD and to STAND OUT.

I am looking for a design to help establish me as an authority for online reputation marketing. This book will be both in Pagely format and be used in print as well.

I am open to questions....

Thanks!

Dale

Reason: I don't believe we have received the right designs. I am going to give everyone more time...

Reason: Hi everyone, I had some stuff come up and was not able to be involved in this project. I am extending because we have not seen the exact thing we want and need time to work with designers to get it right. Thanks Dale

Reason: I am currently traveling and can't wrap this up until I get back.

Target Market(s)

Business Owners

Industry/Entity Type

Business

Requirements
Must have
• Title and Subtitle

Author Name

5 Stars Images....
Nice to have
• Creativity

Bold and stand out

Professional

Should not have
• thin text, small to read text, lame graphics,

```html
<!DOCTYPE html>
<html lang="en">
<head>
<meta charset="utf-8">
<title>Standing Growth – Book Cover</title>
<link rel="stylesheet" href="https://fonts.googleapis.com/css2?family=Bebas+Neue&family=Montserrat:wght@300;800&display=swap">
<style>
  :root {
    --red-bright: #e01010;
    --red-mid: #b00000;
    --red-deep: #5a0000;
    --shadow-red: #3a0000;
    --white: #ffffff;
    --gold-light: #fff6b8;
    --gold: #f3cf3a;
    --gold-dark: #c9951a;
  }
  * { margin: 0; padding: 0; box-sizing: border-box; }
  html, body { width: 800px; height: 1200px; overflow: hidden; background: var(--red-deep); }
  .cover {
    position: relative;
    width: 800px;
    height: 1200px;
    overflow: hidden;
    color: var(--white);
    text-align: center;
  }
  .cover__backdrop {
    position: absolute;
    inset: 0;
    background:
      radial-gradient(ellipse 70% 55% at 50% 48%, var(--red-bright) 0%, var(--red-mid) 45%, var(--red-deep) 100%);
  }
  .kicker {
    position: absolute;
    top: 158px;
    left: 0;
    width: 100%;
  }
  .kicker__main {
    display: block;
    font-family: 'Montserrat', sans-serif;
    font-weight: 800;
    font-size: 46px;
    letter-spacing: -1.5px;
    line-height: 1;
  }
  .kicker__sub {
    display: block;
    margin: 2px 0 0 150px;
    font-family: 'Montserrat', sans-serif;
    font-weight: 300;
    font-size: 21px;
    letter-spacing: -0.5px;
    line-height: 1.1;
  }
  .stars {
    position: absolute;
    left: 0;
    top: 0;
    width: 800px;
    height: 1200px;
  }
  .title {
    position: absolute;
    top: 512px;
    left: 0;
    width: 100%;
    font-family: 'Bebas Neue', sans-serif;
    font-weight: 400;
    font-size: 182px;
    line-height: 0.79;
    letter-spacing: 2px;
    white-space: nowrap;
    text-shadow: 5px 5px 0 var(--shadow-red);
  }
  .title span { display: block; }
  .subtitle {
    position: absolute;
    top: 918px;
    left: 0;
    width: 100%;
    font-family: 'Montserrat', sans-serif;
    font-weight: 300;
    font-size: 21px;
    line-height: 26px;
    letter-spacing: -0.4px;
    white-space: nowrap;
  }
  .subtitle span { display: block; }
  .author {
    position: absolute;
    top: 1110px;
    left: 0;
    width: 100%;
    font-family: 'Bebas Neue', sans-serif;
    font-size: 52px;
    letter-spacing: 11px;
    line-height: 1;
    padding-left: 11px;
    white-space: nowrap;
  }
</style>
</head>
<body>
<main class="cover">
  <div class="cover__backdrop" role="img" aria-label="Red glowing backdrop with a connected network of business people silhouettes"></div>

  <p class="kicker">
    <span class="kicker__main">KEYS TO GLOWING</span>
    <span class="kicker__sub">CUSTOMER RATINGS</span>
  </p>

  <svg class="stars" viewBox="0 0 800 1200" aria-hidden="true">
    <defs>
      <linearGradient id="star-fill" x1="0" y1="0" x2="0" y2="1">
        <stop offset="0" stop-color="var(--gold-light)"/>
        <stop offset="0.55" stop-color="var(--gold)"/>
        <stop offset="1" stop-color="var(--gold-dark)"/>
      </linearGradient>
      <polygon id="star-shape" points="0,-1 0.294,-0.405 0.951,-0.309 0.476,0.155 0.588,0.809 0,0.5 -0.588,0.809 -0.476,0.155 -0.951,-0.309 -0.294,-0.405"
        fill="url(#star-fill)" stroke="#d9a623" stroke-width="3" stroke-linejoin="round" vector-effect="non-scaling-stroke"/>
    </defs>
    <use href="#star-shape" transform="translate(140 450) scale(60)"/>
    <use href="#star-shape" transform="translate(656 450) scale(60)"/>
    <use href="#star-shape" transform="translate(249 420) scale(78)"/>
    <use href="#star-shape" transform="translate(547 420) scale(78)"/>
    <use href="#star-shape" transform="translate(398 406) scale(112)"/>
  </svg>

  <h1 class="title">
    <span>STANDING</span>
    <span>GROWTH</span>
  </h1>

  <p class="subtitle">
    <span>THAT FILL THE CALENDAR</span>
    <span>AND</span>
    <span>DRAW FRESH CLIENTS THROUGH EVERY ENTRANCE!</span>
  </p>

  <p class="author">FIREMAN DALE ORSWORTH</p>
</main>
</body>
</html>
```